Meridale Teen Houses QUILT Poster

We need a poster to put up around our Community/Youth Centers that shows the acronym Q.U.I.L.T. which stands for the traits our that make up the culture and personalities of our youth, families and staff. We would like the color scheme to be in our brand colors, and will send them as an upload (grey, blue, green). The poster must have our logo & tagline (uploaded), which may be small and not central. It should have the acronym with the associated words spelled out - as the smaller descriptive words as shown in uploaded attachment. It should be fun - youth friendly (ages 3-18) and really pop. I have also uploaded a sample poster that we created - but don't like....it feels boring, uninspired. It must say "The MTH" Q.U.I.L.T as QUILT is also the name of a different youth agency and we don't want our acronym to be confused with their name. Finally - to tell you a bit more about our organization I have uploaded our annual report. We can't way to see your ideas!!

Target Market(s)

Internal Information Poster for our community centers

Industry/Entity Type

Education

Other font styles liked:
• FUN

Requirements
Must have
• It must say "The MTH" Q.U.I.L.T as QUILT is also the name of a different youth agency and we don't want our acronym to be confused with their name
• The MTH Q.U.I.L.T. - and associated words - should be dominant/prevalent ....
Nice to have
• Fun Images/photos of actual sparks....
Should not have
• As described w/uploads

```html
<!DOCTYPE html>
<html lang="en">
<head>
<meta charset="utf-8">
<title>The MTH QUILT Poster</title>
<link rel="stylesheet" href="https://fonts.googleapis.com/css2?family=Alfa+Slab+One&family=Open+Sans:wght@400;700&display=swap">
<style>
  :root {
    --paper: #ffffff;
    --band: #8fd0cf;
    --panel: #52b5b5;
    --red: #d63a24;
    --yellow: #f1bd3c;
    --pink: #c766a8;
    --green: #7ab83a;
    --teal: #52b5b5;
    --grey: #6d6e71;
    --white: #ffffff;
  }
  * { margin: 0; padding: 0; box-sizing: border-box; }
  html, body { width: 849px; height: 1200px; overflow: hidden; background: var(--paper); }
  .poster { position: relative; width: 849px; height: 1200px; background: var(--paper); }

  .title-band {
    position: absolute; left: 0; top: 0; width: 849px; height: 152px;
    background: var(--band);
    display: flex; align-items: center; justify-content: center;
  }
  .title {
    font-family: "Alfa Slab One", serif;
    font-size: 108px; line-height: 1; letter-spacing: 6px;
    color: var(--white); font-weight: 400;
  }

  .trait-panel {
    position: absolute; left: 249px; top: 152px; width: 600px; height: 927px;
    background: var(--panel);
  }

  .trait-list { list-style: none; }
  .trait {
    position: absolute; left: 0; width: 849px; height: 152px;
    display: flex; align-items: center;
  }
  .trait-badge {
    position: absolute; left: 80px; top: 4px;
    width: 146px; height: 146px; border-radius: 50%;
    display: flex; align-items: center; justify-content: center;
    font-family: "Alfa Slab One", serif; font-size: 118px; line-height: 1;
    color: var(--white);
    text-shadow: 3px 3px 0 rgba(0,0,0,0.18);
  }
  .trait-rest {
    position: absolute; left: 262px;
    font-family: "Open Sans", sans-serif; font-weight: 700;
    font-size: 86px; line-height: 1; letter-spacing: 0;
    color: var(--white);
  }
  .badge-red { background: var(--red); }
  .badge-yellow { background: var(--yellow); }
  .badge-pink { background: var(--pink); }
  .badge-green { background: var(--green); }
  .badge-teal { background: var(--teal); }

  .trait-q { top: 159px; }
  .trait-u { top: 347px; }
  .trait-i { top: 541px; }
  .trait-l { top: 733px; }
  .trait-t { top: 921px; }

  .org-mark {
    position: absolute; left: 0; top: 1108px; width: 849px;
    display: flex; flex-direction: column; align-items: center;
  }
  .org-line { display: flex; align-items: center; gap: 12px; }
  .org-dot { width: 34px; height: 34px; border-radius: 50%; background: var(--teal); }
  .org-name {
    font-family: "Open Sans", sans-serif; font-weight: 700;
    font-size: 30px; line-height: 1; color: var(--grey); letter-spacing: 0.5px;
  }
  .org-tagline {
    margin-top: 8px; margin-left: 46px;
    font-family: "Open Sans", sans-serif; font-weight: 400;
    font-size: 20px; letter-spacing: 1px; color: var(--grey);
  }
</style>
</head>
<body>
<main class="poster">
  <header class="title-band">
    <h1 class="title">THE MTH</h1>
  </header>

  <section class="trait-panel" aria-hidden="true"></section>

  <ul class="trait-list" aria-label="Q.U.I.L.T. traits">
    <li class="trait trait-q"><span class="trait-badge badge-red">Q</span><span class="trait-rest">UIRKY</span></li>
    <li class="trait trait-u"><span class="trait-badge badge-yellow">U</span><span class="trait-rest">NSTOPPABLE</span></li>
    <li class="trait trait-i"><span class="trait-badge badge-pink">I</span><span class="trait-rest">NSPIRED</span></li>
    <li class="trait trait-l"><span class="trait-badge badge-green">L</span><span class="trait-rest">OYAL</span></li>
    <li class="trait trait-t"><span class="trait-badge badge-teal">T</span><span class="trait-rest">HOUGHTFUL</span></li>
  </ul>

  <footer class="org-mark">
    <div class="org-line">
      <span class="org-dot"></span>
      <span class="org-name">MERIDALE TEEN HOUSES</span>
    </div>
    <p class="org-tagline">WHERE YOUNG IDEAS GROW</p>
  </footer>
</main>
</body>
</html>
```